Lab & Medical Equipment Repair Company Business Card Design

Looking for business card design for a lab & medical equipment repair company. Must be double-sided and must list our primary pieces we repair. Optionally, can include a QR code which should direct to our website.

Clients are usually doctors, so the card must be designed with a professional tone; however, we are looking for creativity in presentation. Open as to what should be on the front and back on card.

** Looking for a CLEAN design with creativity. Please use "Nice to have Priorities" items with discretion.

Core marketing logic:

When lab or medical equipment needs repair, most doctors call the manufacturers and schedule a technician to repair. Usually this takes one or two weeks, and, often, their work spoils. Alternatively, the doctors could hold equipment insurance which gives them a less expensive cost, but the response time is still similarly long.

Our company provides both competitive rates and one of the fastest response times in the industry. Technicians are dispatched directly to the site of the equipment, usually within 24 hours. Equipment under contract receives the same fast response time and includes complimentary annual maintenance. We service some of the most prestigious facilities in the Pittsburgh area and cover all of Western Pennsylvania, Ohio, and West Virginia.

Target Market(s)

Laboratory owners (doctors)

Industry/Entity Type

Marketing

Requirements
Must have
• Company Logo
Employee Name: Ray Dunwoody
Employee Title: CEO
Company Phone: 724-555-0187
Company Fax: 866-555-0143
Company Address: PO Box 518 Harmony Glen, PA 16099
Company Website: www.brightfixlabtech.example
Equipment We Service: Freezers, Cryostorage, Incubators, Centrifuges, Refrigerators, Environmental Chambers, Autoclaves, and more.

Nice to have
• Company Facebook: facebook.com/bfltllc
Company Twitter: @BFLTLLC
QR Code (link to website): www.brightfixlabtech.example

```html
<!DOCTYPE html>
<html lang="en">
<head>
<meta charset="utf-8">
<title>BFLT Business Card</title>
<link rel="stylesheet" href="https://fonts.googleapis.com/css2?family=PT+Sans+Narrow:wght@400;700&display=swap">
<style>
  :root {
    --page-bg: #e9e9e6;
    --card-white: #ffffff;
    --card-shade: #f1f1f1;
    --brand-green: #2dbb5d;
    --brand-green-dark: #1f9e48;
    --brand-green-light: #4fcf78;
    --ink: #2b2b2b;
    --ink-soft: #5f5f5f;
  }
  * { margin: 0; padding: 0; box-sizing: border-box; }
  html, body {
    width: 1200px;
    height: 1023px;
    overflow: hidden;
    background: var(--page-bg);
    font-family: "PT Sans Narrow", "Arial Narrow", sans-serif;
  }
  .canvas {
    position: relative;
    width: 1200px;
    height: 1023px;
  }
  .card {
    position: absolute;
    left: 250px;
    width: 700px;
    height: 400px;
    border-radius: 4px;
    overflow: hidden;
    box-shadow: 0 6px 18px rgba(0,0,0,0.18);
  }

  /* Front side */
  .card--front {
    top: 60px;
    background: linear-gradient(135deg, var(--card-white) 0%, var(--card-shade) 100%);
  }
  .logo {
    position: absolute;
    top: 64px;
    left: 300px;
    display: flex;
    align-items: center;
    gap: 12px;
  }
  .logo__dot {
    width: 16px;
    height: 16px;
    border-radius: 50%;
    background: var(--brand-green);
  }
  .logo__name {
    font-size: 56px;
    font-weight: 700;
    letter-spacing: 6px;
    color: var(--ink);
  }
  .name-tab {
    position: absolute;
    left: 0;
    top: 196px;
    width: 290px;
    height: 80px;
    border-radius: 0 40px 40px 0;
    background: linear-gradient(180deg, var(--brand-green-light) 0%, var(--brand-green) 100%);
    padding: 12px 0 0 36px;
    color: var(--card-white);
  }
  .name-tab__name {
    font-size: 30px;
    line-height: 1.05;
  }
  .name-tab__title {
    font-size: 16px;
    opacity: 0.9;
  }
  .contact {
    position: absolute;
    left: 36px;
    top: 292px;
    font-size: 18px;
    line-height: 1.4;
    color: var(--ink-soft);
  }
  .contact__label {
    color: var(--brand-green);
    font-weight: 700;
    margin-right: 5px;
  }
  .contact__gap { margin-left: 12px; }
  .contact__address {
    color: var(--ink);
    font-weight: 700;
    font-size: 19px;
  }
  .website {
    position: absolute;
    right: 40px;
    bottom: 38px;
    font-size: 18px;
    letter-spacing: 1.5px;
    color: var(--ink);
  }

  /* Back side */
  .card--back {
    top: 540px;
    background: linear-gradient(135deg, var(--brand-green-light) 0%, var(--brand-green) 55%, var(--brand-green-dark) 100%);
    color: var(--card-white);
  }
  .services {
    position: absolute;
    left: 48px;
    right: 48px;
    top: 34px;
  }
  .services__heading {
    font-size: 28px;
    font-weight: 700;
    letter-spacing: 1px;
    margin-bottom: 14px;
  }
  .services__list {
    list-style: none;
    display: grid;
    grid-template-columns: repeat(3, 1fr);
    row-gap: 6px;
    font-size: 20px;
  }
  .services__list li::before {
    content: "";
    display: inline-block;
    width: 8px;
    height: 8px;
    margin-right: 10px;
    border-radius: 50%;
    background: var(--card-white);
    vertical-align: middle;
  }
  .back-band {
    position: absolute;
    left: 0;
    right: 0;
    top: 250px;
    height: 70px;
    background: var(--card-white);
    display: flex;
    align-items: center;
    justify-content: space-between;
    padding: 0 48px;
    font-size: 18px;
    color: var(--ink);
  }
  .back-band__web {
    font-weight: 700;
    letter-spacing: 1px;
  }
  .back-band__label {
    color: var(--brand-green);
    font-weight: 700;
    margin-right: 5px;
  }
</style>
</head>
<body>
  <main class="canvas">
    <section class="card card--front">
      <div class="logo">
        <span class="logo__dot"></span>
        <span class="logo__name">BFLT</span>
      </div>
      <div class="name-tab">
        <p class="name-tab__name">Ray Dunwoody</p>
        <p class="name-tab__title">CEO</p>
      </div>
      <div class="contact">
        <p><span class="contact__label">T</span>724-555-0187<span class="contact__gap contact__label">F</span>866-555-0143</p>
        <p><span class="contact__label">E</span>ray@brightfixlabtech.example</p>
        <p class="contact__address">PO Box 518 Harmony Glen, PA 16099</p>
      </div>
      <p class="website">www.brightfixlabtech.example</p>
    </section>

    <section class="card card--back">
      <div class="services">
        <h2 class="services__heading">Equipment We Service</h2>
        <ul class="services__list">
          <li>Freezers</li>
          <li>Cryostorage</li>
          <li>Incubators</li>
          <li>Centrifuges</li>
          <li>Refrigerators</li>
          <li>Environmental Chambers</li>
          <li>Autoclaves</li>
          <li>and more</li>
        </ul>
      </div>
      <div class="back-band">
        <span class="back-band__web">www.brightfixlabtech.example</span>
        <span><span class="back-band__label">f</span>facebook.com/bfltllc</span>
        <span><span class="back-band__label">t</span>@BFLTLLC</span>
      </div>
    </section>
  </main>
</body>
</html>
```